Business card for Tolvery Anesthesia LLC

This is for a business care for Tolvery Anesthesia LLC. Dr. Lisbeth Tolvery, CRNA, DNAP is the sole provider in the LLC. Business address is 4718 N Brackley Street,
Oakhaven, PA 17342
CRNA stands for certified registered nurse anesthetist
"Keeping you safe and comfortable"
I plan to give this business card to the patients that I provide anesthesia to.
Creative design that ties into Anesthesia. Calm soothing colors.

Target Market(s)

Business card for my patients.

Industry/Entity Type

Medicine

Contact Information for Business Card

Creative, professional, eye catching

Logo Text

Tolvery Anesthesia

Font styles to use
Serif
Script

Colors

Designer to choose colors to be used in the design.

Requirements
Must have
• Tolvery Anesthesia
• Dr. Lisbeth Tolvery, CRNA, DNAP
• tolvery.anesthesia@ quillmail.net
Nice to have
• "Keeping you safe and comfortable"
Should not have
• phone number

```html
<!DOCTYPE html>
<html lang="en">
<head>
<meta charset="utf-8">
<title>Tolvery Anesthesia — Business Card</title>
<link href="https://fonts.googleapis.com/css2?family=Noto+Serif:wght@400;700&display=swap" rel="stylesheet">
<style>
  :root {
    --page: #ffffff;
    --card: #c5e2f2;
    --ink: #0c0c0c;
    --art-light: #dff0fa;
    --art-teal: #3cbfd9;
    --art-skin: #fcd6a8;
  }
  html, body {
    margin: 0;
    padding: 0;
    width: 904px;
    height: 1200px;
    overflow: hidden;
    background: var(--page);
  }
  .sheet {
    position: relative;
    width: 904px;
    height: 1200px;
    font-family: "Noto Serif", Georgia, serif;
    color: var(--ink);
  }
  .card {
    position: absolute;
    background: var(--card);
    border-radius: 34px;
  }
  .card--front { left: 0; top: 0; width: 889px; height: 543px; }
  .card--back  { left: 15px; top: 656px; width: 888px; height: 542px; }

  .illustration {
    position: absolute;
    width: 226px;
    height: 205px;
    border-radius: 18px;
    background: linear-gradient(180deg, var(--art-light) 0%, var(--art-teal) 60%, var(--art-skin) 100%);
    opacity: 0.85;
  }
  .card--front .illustration { left: 332px; top: 33px; }
  .card--back  .illustration { left: 319px; top: 147px; }

  .brand {
    position: absolute;
    left: 0; width: 882px;
    top: 272px;
    text-align: center;
    font-size: 30px;
    font-weight: 400;
    margin: 0;
    line-height: 1.2;
  }
  .provider {
    position: absolute;
    left: 0; width: 954px;
    top: 309px;
    text-align: center;
    font-size: 37px;
    font-weight: 700;
    margin: 0;
    line-height: 1.2;
  }
  .contact {
    position: absolute;
    left: 252px;
    top: 380px;
    display: flex;
    align-items: center;
    gap: 11px;
    font-size: 22.5px;
    line-height: 1;
  }
  .contact svg { width: 31px; height: 23px; }
  .tagline {
    position: absolute;
    left: 0;
    width: 100%;
    text-align: center;
    font-size: 22.5px;
    margin: 0;
    line-height: 1.2;
  }
  .card--front .tagline { top: 497px; left: 0; width: 888px; }
  .card--back  .tagline { top: 364px; }
</style>
</head>
<body>
<main class="sheet">
  <section class="card card--front">
    <div class="illustration" role="img" aria-label="Illustration of an anesthesia provider in scrub cap and surgical mask"></div>
    <h2 class="brand">Tolvery Anesthesia</h2>
    <h1 class="provider">Dr. Lisbeth Tolvery, CRNA, DNAP</h1>
    <div class="contact">
      <svg viewBox="0 0 31 23" aria-hidden="true">
        <rect x="1" y="1" width="29" height="21" fill="none" stroke="var(--ink)" stroke-width="1.8"/>
        <path d="M1 1 L15.5 13 L30 1 M1 22 L12 10 M30 22 L19 10" fill="none" stroke="var(--ink)" stroke-width="1.8"/>
      </svg>
      <span class="email">tolvery.anesthesia@ quillmail.net</span>
    </div>
    <p class="tagline">Keeping you safe and comfortable</p>
  </section>

  <section class="card card--back">
    <div class="illustration" role="img" aria-label="Illustration of an anesthesia provider in scrub cap and surgical mask"></div>
    <p class="tagline">Keeping you safe and comfortable</p>
  </section>
</main>
</body>
</html>
```